Torvel Law, PC Letterhead Design -- LAW FIRM

I am looking for a very elegant letterhead design for my personal injury law practice.
The letter head must have 4 different variations of the same thing meaning one design that has just a header, and another with a header and footer.
Elegance is key, I do not want it to be too bold. Please stay away from colors that are not black, white or gray or silver.
Please include a gradient style letterhead for the header while implementing the design of the logo found in folder #3
I have attached for you the logos and emblems for my company below.
In folders 1-4 you will find my actual logo.
In folder 5-6 you will find a shorter version of my logo, this can be implemented maybe in the footer + header design of the letter head (do not include this shortened version in the header).
In folders 7-8 you will find an emblem for my company.
Information that needs to be found on the letterhead is as follows:
A clearly written version of my company name: Torvel Law, PC
Address: 4718 Pemberly Avenue Suite #512, Beverly Hills, CA, 90210
Email: dorian@torvellaw.example
Telephone number: 310-555-0174

```html
<!DOCTYPE html>
<html lang="en">
<head>
<meta charset="utf-8">
<title>Torvel Law, PC — Letterhead</title>
<link rel="stylesheet" href="https://fonts.googleapis.com/css2?family=Public+Sans:wght@400;500&display=swap">
<style>
  :root {
    --paper: #f5f6f8;
    --ink: #111111;
    --band: #000000;
    --rule: #1a1a1a;
    --emblem-tone: #2b2b2b;
    --signature-tone: #3a3a3a;
  }
  * { margin: 0; padding: 0; box-sizing: border-box; }
  html, body { width: 927px; height: 1200px; overflow: hidden; background: var(--paper); }
  .letterhead {
    position: relative;
    width: 927px;
    height: 1200px;
    background: var(--paper);
    font-family: "Public Sans", Arial, sans-serif;
    color: var(--ink);
    overflow: hidden;
  }
  .corner { position: absolute; display: block; }
  .corner path { fill: var(--band); }
  .corner--top { top: 0; right: 0; }
  .corner--bottom { bottom: 0; left: 0; }

  .firm-name {
    position: absolute;
    left: 77px;
    top: 118px;
    font-size: 34px;
    font-weight: 400;
    letter-spacing: 0.5px;
    color: var(--ink);
  }

  .sidebar { position: absolute; left: 53px; width: 204px; font-size: 14.5px; line-height: 20px; }
  .sidebar__rule { height: 0; border-top: 1.5px solid var(--rule); }
  .sidebar--address { top: 306px; }
  .sidebar--contact { top: 481px; }
  .sidebar address { font-style: normal; margin-top: 18px; }
  .sidebar .contact-list { list-style: none; margin-top: 18px; }

  .emblem {
    position: absolute;
    left: 77px;
    top: 893px;
    width: 78px;
    height: 60px;
    background: var(--emblem-tone);
    border-radius: 4px;
  }

  .letter-body {
    position: absolute;
    left: 299px;
    top: 299px;
    width: 560px;
    font-size: 13.6px;
    line-height: 19.75px;
  }
  .letter-body p + p { margin-top: 19.75px; }
  .letter-body p.tight { margin-top: 0; }

  .signature {
    position: absolute;
    left: 668px;
    top: 1012px;
    width: 162px;
    height: 46px;
    background: var(--signature-tone);
    border-radius: 4px;
  }
</style>
</head>
<body>
<main class="letterhead">
  <svg class="corner corner--top" width="400" height="210" viewBox="527 0 400 210" aria-hidden="true">
    <path d="M527 0 H927 V207 H812 C786 207 770 194 770 170 C770 150 756 140 735 140 H705 C676 140 657 124 657 98 C657 80 645 73 625 70 C575 60 527 40 527 0 Z"/>
  </svg>

  <h1 class="firm-name">Torvel Law, PC</h1>

  <section class="sidebar sidebar--address">
    <div class="sidebar__rule"></div>
    <address>4718 Pemberly Avenue,<br>Suite #512,<br>Beverly Hills, CA, 90210</address>
  </section>

  <section class="sidebar sidebar--contact">
    <div class="sidebar__rule"></div>
    <ul class="contact-list">
      <li>310-555-0174</li>
      <li>dorian@torvellaw.example</li>
    </ul>
  </section>

  <div class="emblem" role="img" aria-label="Firm emblem: scales of justice"></div>

  <article class="letter-body">
    <p>Lorem ipsum dolor sit amet, consectetuer adipiscing elit, sed diam nonummy nibh euismod tincidunt ut laoreet dolore magna aliquam erat volutpat. Ut wisi enim ad minim veniam, quis nostrud exerci tation ullamcorper<br>suscipit lobortis nisl ut aliquip ex ea commodo consequat. Duis autem vel eum iriure dolor in hendrerit in vulputate velit esse molestie consequat, vel illum dolore eu feugiat nulla facilisis at vero eros et accumsan et iusto odio dignissim qui blandit praesent luptatum zzril delenit augue duis dolore te feugait nulla facilisi.</p>
    <p>Lorem ipsum dolor sit amet, consectetuer adipiscing elit, sed diam nonummy nibh euismod tincidunt ut laoreet dolore magna aliquam erat volutpat. Ut wisi enim ad minim veniam, quis nostrud exerci tation ullamcorper suscipit lobortis nisl ut aliquip ex ea commodo consequat. Duis autem vel eum iriure dolor in hendrerit in vulputate velit esse molestie consequat, vel illum dolore eu feugiat nulla facilisis at vero eros et accumsan et iusto odio dignissim qui blandit prae-<br>sent luptatum zzril delenit augue duis dolore te feugait nulla facilisi.</p>
    <p class="tight">Lorem ipsum dolor sit amet, cons ectetuer adipiscing elit, sed diam nonummy nibh euismod tincidunt ut laoreet dolore magna aliquam erat volutpat. Ut wisi enim ad minim veniam, quis nostrud exerci tation ullamcorper<br>suscipit lobortis nisl ut aliquip ex ea commodo consequat.</p>
    <p>Lorem ipsum dolor sit amet, consectetuer adipiscing elit, sed diam nonummy nibh euismod tincidunt ut laoreet dolore magna aliquam erat volutpat. Ut wisi enim ad minim veniam, quis nostrud exerci tation ullamcorper suscipit lobortis nisl ut aliquip ex ea commodo consequat. Duis autem vel eum iriure dolor in hendrerit in vulputate velit esse molestie consequat, vel illum dolore eu feugiat nulla facilisis at vero eros et accumsan et iusto odio dignissim qui blandit prae-<br>sent luptatum zzril delenit augue duis dolore te feugait nulla facilisi.</p>
    <p>Lorem ipsum dolor sit amet, cons ectetuer adipiscing elit, sed diam nonummy nibh euismod tincidunt ut laoreet dolore magna aliquam erat volutpat. Ut wisi enim ad minim veniam, quis nostrud exerci tation ullamcorper suscipit lobortis nisl ut aliquip ex ea commodo consequat.</p>
  </article>

  <div class="signature" role="img" aria-label="Handwritten signature"></div>

  <svg class="corner corner--bottom" width="280" height="135" viewBox="0 1065 280 135" aria-hidden="true">
    <path d="M0 1067 H98 C116 1067 125 1079 125 1095 C125 1114 140 1125 165 1125 H198 C218 1125 232 1138 242 1150 C256 1166 266 1182 275 1200 H0 Z"/>
  </svg>
</main>
</body>
</html>
```